Website redesign for a technology and engineering company

We'd like to redesign our website which can be found on brovalux.co.nz
!! Please find the designers brief as an uploaded file with all details in there!!
The main purpose for redesign is:
>change of services offered
>old website not very user friendly to maintain or update
Key requirements:
>visually appealing
>easy to navigate
>simple and easy to read
>responsive
>mobile device compatibility
>integrating best SEO practice
All the details are in the attached designer brief document.

Coding
Coded - Design and coding required
Number of Pages Required
1 page
Look and feel
Each slider illustrates characteristics of the customer's brand and the style your logo design should communicate.

```html
<!DOCTYPE html>
<html lang="en">
<head>
<meta charset="utf-8">
<title>Brovalux — Precision. Efficiency. Clarity.</title>
<link rel="stylesheet" href="https://fonts.googleapis.com/css2?family=Mulish:ital,wght@0,400;0,500;0,600;0,700;1,500&family=Oswald:wght@400&display=swap">
<style>
:root{
  --blue:#3f6ff2;
  --ink:#111418;
  --text:#2b2f36;
  --soft:#f4f4f4;
  --white:#ffffff;
  --slate:#3c5668;
  --ring:#4c6a7c;
  --icon:#2a2d33;
}
*{box-sizing:border-box;margin:0;padding:0}
html,body{width:1200px;height:3589px;overflow:hidden}
body{font-family:"Mulish",sans-serif;color:var(--text);background:var(--white);position:relative}
.abs{position:absolute}
.btn{position:absolute;display:flex;align-items:center;justify-content:center;background:var(--blue);color:var(--white);border-radius:22px;font-size:14px;font-weight:500;box-shadow:0 3px 8px rgba(40,80,200,.25);text-decoration:none}
.section-title{position:absolute;left:0;width:1200px;text-align:center;font-size:38px;font-weight:500;color:var(--ink)}
.rule{position:absolute;height:2px;background:var(--ink)}

/* hero */
.hero{position:absolute;left:0;top:0;width:1200px;height:599px;background:linear-gradient(180deg,#6f7f96 0%,#93a2b6 28%,#8a8a86 58%,#5d5a52 100%)}
.hero-photo{position:absolute;inset:0;background:linear-gradient(100deg,rgba(60,66,78,.55) 0%,rgba(60,66,78,.1) 55%,rgba(0,0,0,0) 100%)}
.brand-mark{position:absolute;left:162px;top:36px;color:var(--white);font-size:34px;font-weight:600;display:flex;align-items:center;gap:10px}
.brand-mark .dot{width:14px;height:14px;border-radius:50%;background:var(--white)}
.nav a{position:absolute;top:43px;color:var(--white);font-size:14px;text-decoration:none}
.hero h1{position:absolute;left:162px;top:214px;font-family:"Oswald",sans-serif;font-weight:400;font-size:39px;color:var(--white);letter-spacing:.3px}
.hero p{position:absolute;left:162px;top:275px;width:405px;font-size:19.5px;line-height:27px;color:var(--white)}

/* services */
.svc-circle{position:absolute;width:196px;height:196px;border-radius:50%;border:4px solid #a9a9a9;background:#f6f6f6;display:flex;flex-direction:column;align-items:center;justify-content:center;text-align:center;font-size:15px;font-weight:600;color:var(--ink);line-height:20px}
.svc-circle.active{border-color:var(--blue);background:var(--white)}
.svc-icon{margin-bottom:6px}
.svc-num{position:absolute;width:36px;height:36px;border-radius:50%;background:#9a9a9a;color:var(--white);font-size:16px;display:flex;align-items:center;justify-content:center;border:3px solid #fff}
.svc-num.active{background:var(--blue)}
.svc-detail h3{position:absolute;left:757px;top:787px;color:var(--blue);font-size:18px;font-weight:500}
.svc-list{position:absolute;left:694px;top:836px;list-style:none;font-size:13.5px;line-height:29.7px;color:var(--ink)}
.svc-list li::before{content:"• "}

/* welcome */
.welcome{position:absolute;left:0;top:1273px;width:1200px;height:418px;background:var(--soft)}
.welcome-art{position:absolute;left:163px;top:62px;width:421px;height:206px;border-radius:103px;background:linear-gradient(120deg,#2c3a2e,#6d7f86 45%,#9aa8b3 60%,#3f4d3c)}
.years{position:absolute;left:163px;top:290px;width:421px;text-align:center;color:var(--blue);font-style:italic;font-weight:500;font-size:31px;letter-spacing:.5px}
.welcome h2{position:absolute;left:626px;top:50px;font-size:38px;font-weight:500;color:var(--ink)}
.welcome .copy{position:absolute;left:626px;top:117px;width:414px;font-size:13.5px;line-height:22px;color:var(--ink)}

/* team banner */
.team{position:absolute;left:0;top:1691px;width:1200px;height:453px;background:linear-gradient(100deg,#4a4e52 0%,#3a4034 45%,#2f3a2a 75%,#3d4437 100%)}
.team p{position:absolute;left:0;top:125px;width:1200px;text-align:center;color:var(--white);font-size:30px;line-height:39px}

/* case studies */
.cases{position:absolute;left:0;top:2144px;width:1200px;height:581px;background:#f6f6f6}
.cases h3{position:absolute;left:164px;top:180px;color:var(--blue);font-size:22px;font-weight:500;line-height:28px;letter-spacing:.3px}
.cases .copy{position:absolute;left:163px;top:248px;width:420px;font-size:13px;line-height:21.6px;color:var(--ink)}
.case-photo{position:absolute;left:622px;top:158px;width:416px;height:330px;border-radius:8px;background:linear-gradient(180deg,#274fa5 0%,#5f85c8 35%,#b9b9b4 55%,#7e7d76 100%)}
.dot-nav{position:absolute;top:300px;width:13px;height:13px;border-radius:50%;background:var(--white)}

/* contact */
.contact{position:absolute;left:0;top:2725px;width:1200px;height:815px;background:linear-gradient(180deg,var(--slate) 0%,#48657a 55%,#5a7387 100%)}
.accent-block{position:absolute;left:149px;top:150px;width:94px;height:94px;background:rgba(255,255,255,.14)}
.portrait-ring{position:absolute;left:129px;top:115px;width:488px;height:488px;border-radius:50%;background:var(--ring);opacity:.75}
.portrait{position:absolute;left:164px;top:150px;width:418px;height:418px;border-radius:50%;background:linear-gradient(160deg,#6d7f8e 0%,#a3a7a5 40%,#c9692f 75%,#6a6f6d 100%)}
.contact h2{position:absolute;left:658px;top:140px;font-size:38px;font-weight:500;color:var(--white)}
.field{position:absolute;left:669px;width:368px;height:41px;background:var(--white);border-radius:3px;display:flex;align-items:center;padding-left:12px;gap:10px;font-size:12.5px;color:#333}
.field svg{flex:none}
.field.msg{height:63px;align-items:flex-start;padding-top:11px}
.info{position:absolute;top:670px;color:var(--white);font-size:12px;line-height:17px}
.info b{font-weight:500;display:block}
.footer-rule{position:absolute;left:163px;top:726px;width:590px;height:1px;background:rgba(255,255,255,.35)}
.follow{position:absolute;left:163px;top:746px;color:var(--white);font-size:13.5px}
.social{position:absolute;left:263px;top:742px;width:26px;height:26px;background:var(--white)}
.foot-brand{position:absolute;left:813px;top:680px;color:var(--white);font-size:52px;font-weight:600;display:flex;align-items:center;gap:12px}
.foot-brand .dot{width:22px;height:22px;border-radius:50%;background:var(--white)}
.copyright{position:absolute;left:0;top:3540px;width:1200px;height:49px;background:var(--blue);color:var(--white);font-size:13px;display:flex;align-items:center;justify-content:center}
</style>
</head>
<body>

<header class="hero">
  <div class="hero-photo" role="img" aria-label="Solar-powered monitoring station on a rocky alpine ridge under a blue sky"></div>
  <div class="brand-mark"><span class="dot"></span>Brovalux</div>
  <nav class="nav">
    <a style="left:565px">Services offered</a>
    <a style="left:704px">Case Studies</a>
    <a style="left:821px">About Us</a>
  </nav>
  <a class="btn" style="left:905px;top:29px;width:132px;height:46px">Get In Touch</a>
  <h1>Precision. Efficiency. Clarity.</h1>
  <p>Solving Field Problems, Build Robust Infrastructure, And Deliver Accurate Data To Clients</p>
  <a class="btn" style="left:162px;top:372px;width:130px;height:43px">Get In Touch</a>
</header>

<section class="services">
  <h2 class="section-title" style="top:676px">Services Offered</h2>
  <div class="rule" style="left:562px;top:735px;width:77px"></div>

  <div class="svc-circle" style="left:209px;top:776px">
    <svg class="svc-icon" width="62" height="52" viewBox="0 0 62 52" aria-hidden="true">
      <g fill="none" stroke="var(--icon)" stroke-width="2.2" stroke-linecap="round" stroke-linejoin="round">
        <path d="M4 14a8 8 0 0 1 16 0z"/><path d="M3 14h18"/>
        <path d="M5 50V30a7 7 0 0 1 14 0v20"/><path d="M12 24v26"/>
        <path d="M36 12h10v8H36z"/><path d="M41 20l-9 30M41 20v30M41 20l9 30"/>
        <path d="M53 8v36M58 8v36M53 14h5M53 26h5M53 38h5"/>
      </g>
    </svg>
    Fieldwork<br>Solutions
  </div>
  <div class="svc-num" style="left:210px;top:916px">1</div>
  <div class="svc-circle active" style="left:432px;top:776px">
    <svg class="svc-icon" width="60" height="56" viewBox="0 0 60 56" aria-hidden="true">
      <g fill="none" stroke="var(--icon)" stroke-width="2.2" stroke-linecap="round" stroke-linejoin="round">
        <path d="M28 50S12 34 12 22a16 16 0 0 1 32 0c0 12-16 28-16 28z"/>
        <circle cx="28" cy="22" r="6"/>
        <path d="M44 8a10 10 0 0 1 6 8M48 3a16 16 0 0 1 8 12"/>
        <path d="M18 54h20"/>
      </g>
    </svg>
    Positioning<br>And Monitoring
  </div>
  <div class="svc-num active" style="left:433px;top:916px">2</div>
  <div class="svc-circle" style="left:320px;top:968px">
    <svg class="svc-icon" width="62" height="54" viewBox="0 0 62 54" aria-hidden="true">
      <g fill="none" stroke="var(--icon)" stroke-width="2.2" stroke-linecap="round" stroke-linejoin="round">
        <path d="M4 10h40v40H4z"/><path d="M4 10a5 5 0 0 1 5-5h30"/>
        <circle cx="24" cy="30" r="6"/>
        <path d="M24 20v3M24 37v3M14 30h3M31 30h3M17 23l2 2M29 35l2 2M31 23l-2 2M17 37l2-2"/>
        <path d="M52 4h6v38l-3 6-3-6z"/><path d="M52 10h6"/>
      </g>
    </svg>
    Design And<br>Prototyping
  </div>
  <div class="svc-num" style="left:321px;top:1107px">3</div>

  <div class="svc-detail">
    <svg class="abs" style="left:692px;top:776px" width="48" height="48" viewBox="0 0 48 48" aria-hidden="true"><circle cx="24" cy="24" r="24" fill="#ececec"/><path d="M24 36s-8-8-8-14a8 8 0 0 1 16 0c0 6-8 14-8 14z" fill="none" stroke="#444" stroke-width="2"/><circle cx="24" cy="22" r="3" fill="none" stroke="#444" stroke-width="2"/></svg>
    <h3>Positioning And Monitoring</h3>
    <ul class="svc-list">
      <li>Real-Time Kinematic (RTK) Solutions</li>
      <li>Custom GNSS Base stations</li>
      <li>NTRIP service</li>
      <li>Tailored Monitoring Solutions</li>
      <li>Environmental Monitoring</li>
      <li>Robust communication Systems</li>
      <li>Internet of Things (IoT) Integration</li>
      <li>Solar powered systems</li>
      <li>Smart Sensor Networks</li>
    </ul>
    <a class="btn" style="left:693px;top:1115px;width:131px;height:43px">Get In Touch</a>
  </div>
</section>

<section class="welcome">
  <div class="welcome-art" role="img" aria-label="Mountain landscape with a monitoring station"></div>
  <div class="years">15+ Years of Experience</div>
  <h2>Welcome to Brovalux</h2>
  <div class="rule" style="left:626px;top:104px;width:74px"></div>
  <div class="copy">
    <p>Your reliable partner in delivering innovative solutions. Our team of skilled professionals is committed to excellence, ensuring every project is handled with precision, efficiency and integrity. We solve problems in the field, build robust infrastructure, and deliver accurate data to our clients.</p>
    <p style="margin-top:3px;margin-left:-3px">Let us help you achieve your goals with our tailored, sustainable solutions and exceptional service</p>
  </div>
  <a class="btn" style="left:624px;top:291px;width:132px;height:43px">Get In Touch</a>
</section>

<section class="team" role="img" aria-label="Technician checking a solar-powered equipment cabinet by a roadside">
  <p>Our Team Ensures Seamless Integration of<br>Cutting-edge Technology To Optimize Performance<br>And Exceed Client Expectations</p>
  <a class="btn" style="left:534px;top:262px;width:131px;height:42px">Get In Touch</a>
</section>

<section class="cases">
  <h2 class="section-title" style="top:78px">Recent Case Studies</h2>
  <div class="rule" style="left:581px;top:136px;width:75px"></div>
  <h3>Remote Camera Installation<br>In Alpine Environment</h3>
  <div class="copy">
    <p>Successful installation of advanced camera systems in the challenging and remote alpine regions of Fiordland.</p>
    <p style="margin-top:4px">This installation supports Skyframe Imaging Ltd in their environmental monitoring efforts, providing high-quality imagery and data to the Regional Conservation Trust from one of the most rugged and inaccessible areas in New Zealand.</p>
  </div>
  <a class="btn" style="left:163px;top:401px;width:131px;height:43px">Get In Touch</a>
  <div class="case-photo" role="img" aria-label="Solar-powered camera station on rocky alpine terrain">
    <span class="dot-nav" style="left:168px"></span>
    <span class="dot-nav" style="left:189px;background:var(--blue)"></span>
    <span class="dot-nav" style="left:210px"></span>
  </div>
</section>

<section class="contact">
  <div class="accent-block" role="img" aria-label="Decorative dot grid accent"></div>
  <div class="portrait-ring"></div>
  <div class="portrait" role="img" aria-label="Team member in high-visibility clothing at an alpine field site"></div>
  <h2>Send Us a Message</h2>
  <div class="rule" style="left:658px;top:196px;width:74px;background:#fff"></div>

  <div class="field" style="top:219px"><svg width="14" height="14" viewBox="0 0 14 14"><circle cx="7" cy="4.5" r="3" fill="none" stroke="#3f6ff2"/><path d="M1.5 13c0-3 2.5-4.5 5.5-4.5s5.5 1.5 5.5 4.5z" fill="none" stroke="#3f6ff2"/></svg>Your Name*</div>
  <div class="field" style="top:274px"><svg width="15" height="12" viewBox="0 0 15 12"><rect x=".5" y=".5" width="14" height="11" fill="none" stroke="#3f6ff2"/><path d="M.5 .5l7 6 7-6" fill="none" stroke="#3f6ff2"/></svg>Your Email*</div>
  <div class="field" style="top:330px"><svg width="14" height="14" viewBox="0 0 14 14"><path d="M3 1l2 3-1.5 1.5c.8 2 2.5 3.6 4.5 4.5L9.5 8.5l3 2-1 2.5C6 13 1 8 1 2.5z" fill="none" stroke="#3f6ff2"/></svg>Your Phone*</div>
  <div class="field" style="top:386px"><svg width="14" height="14" viewBox="0 0 14 14"><path d="M2 12l1-4 7-7 3 3-7 7z" fill="none" stroke="#3f6ff2"/></svg>Inquiry For*<svg style="margin-left:auto;margin-right:12px" width="12" height="8" viewBox="0 0 12 8"><path d="M1 7l5-5 5 5" fill="none" stroke="#333" stroke-width="1.5"/></svg></div>
  <div class="field msg" style="top:440px"><svg width="14" height="13" viewBox="0 0 14 13"><ellipse cx="7" cy="5.5" rx="6" ry="4.5" fill="none" stroke="#3f6ff2"/><path d="M3 9l-1 3 3-2" fill="none" stroke="#3f6ff2"/></svg>Message*</div>
  <a class="btn" style="left:669px;top:518px;width:148px;height:39px;font-size:15px">Send Message</a>

  <svg class="abs" style="left:162px;top:671px" width="18" height="26" viewBox="0 0 18 26"><path d="M9 1C4.6 1 1 4.6 1 9c0 6 8 16 8 16s8-10 8-16c0-4.4-3.6-8-8-8z" fill="none" stroke="#6f97ff" stroke-width="1.5"/><circle cx="9" cy="9" r="3" fill="none" stroke="#6f97ff" stroke-width="1.5"/></svg>
  <div class="info" style="left:187px"><b>Address</b>Street Name NewZealand 45620</div>
  <svg class="abs" style="left:437px;top:671px" width="26" height="26" viewBox="0 0 26 26"><path d="M6 2l4 6-3 3c1.5 3.5 4.5 6.5 8 8l3-3 6 4-2 5C11 25 1 15 1 4z" fill="none" stroke="#6f97ff" stroke-width="1.5"/></svg>
  <div class="info" style="left:475px"><b>Phone</b>123.456.7890</div>
  <svg class="abs" style="left:618px;top:673px" width="26" height="22" viewBox="0 0 26 22"><rect x="1" y="6" width="24" height="15" fill="none" stroke="#6f97ff" stroke-width="1.5"/><path d="M1 6l12 9 12-9" fill="none" stroke="#6f97ff" stroke-width="1.5"/></svg>
  <div class="info" style="left:651px"><b>Email</b>hi@brovalux.co.nz</div>
  <div class="footer-rule"></div>
  <div class="follow">Follow Us On</div>
  <div class="social" aria-label="Social profile"></div>
  <div class="foot-brand"><span class="dot"></span>Brovalux</div>
</section>

<footer class="copyright">© 2024. Brovalux All Rights Reserved</footer>

</body>
</html>
```